Brochure Design Project

I require a brochure with inserts inside that show our different services for different industries.

The insides of the brochure will have "about our company" ie, trackered vans - pda's and software used - images of the team and showing we invest in the very latest equipment and softwares to offer the best highest quality service. etc etc then the inserts demonstrating what we can do for each industry - images working on sites, equipment used etc etc on the back of each sheet a case study proving implementation.

Construction
Public Transport
Hotel & Leisure
Retail / Businesses
Housing Association

The inserts I imagine will be different in size or cut differently down the sides in order to allow the reader to see the different sectors and go to the one they require. The brochure will go in full to some companies - like facilities management whom would be interested in all the work we do for industries - however the brochure may contain just one of the inserts if we visit say a construction site in which they would only be interested in one (construction)

The inserts will show all the services we offer for that industry and maybe to the rear have a case study in which proves our implementation of service.

Our overall company is to offer solutions for damaged , worn or complete change of style to surfaces. For example we offer invisible damage repairs to surfaces like woods, laminates, ceramics etc.
We offer full scale resurfacing from bath re-enamelling to commercial spraying of powdercoating, metal work on offices.

also must have slot for business card.

Our communication to the customer is that using our services you can repair or resurface items back to new at the fraction of the cost of replacement thus reducing landfil as you are replacing not repairing. You get the brand new finish for a lot less cost - time and mess.

VELTIQ - cutting cost with the environment in mind.

Target Market(s)

Various sectors as indicated. Business card slot.

Industry/Entity Type

Communication

Requirements
Must have
• inserts cut down the side in a way that looks good when one single insert is added but all look great showing through each sector when all added together.

```html
<!DOCTYPE html>
<html lang="en">
<head>
<meta charset="utf-8">
<title>VELTIQ – Company Brochure</title>
<link href="https://fonts.googleapis.com/css2?family=Cabin:wght@600&family=Cabin+Condensed:wght@500&family=Lato:ital,wght@0,300;0,400;1,400&family=Open+Sans:wght@400&display=swap" rel="stylesheet">
<style>
  :root {
    --ink: #000000;
    --paper: #ffffff;
    --leaf: #8cc63f;
    --mist: #d9d9d9;
  }
  html, body {
    margin: 0;
    padding: 0;
    overflow: hidden;
    background: var(--ink);
  }
  .cover {
    position: relative;
    width: 848px;
    height: 1200px;
    background: var(--ink);
    overflow: hidden;
  }
  .brand-mark {
    position: absolute;
    left: 330px;
    top: 150px;
    width: 160px;
    height: 160px;
    border-radius: 50%;
    border: 14px solid var(--paper);
    box-sizing: border-box;
  }
  .brand-name {
    position: absolute;
    left: 0;
    width: 728px;
    top: 392px;
    margin: 0;
    text-align: center;
    font-family: "Cabin", sans-serif;
    font-weight: 600;
    font-size: 142px;
    line-height: 1;
    letter-spacing: 4px;
    color: var(--paper);
  }
  .services-line {
    position: absolute;
    left: 0;
    width: 728px;
    top: 622px;
    margin: 0;
    text-align: center;
    font-family: "Cabin Condensed", sans-serif;
    font-weight: 500;
    font-size: 27px;
    letter-spacing: 2px;
    color: var(--leaf);
  }
  .slogan {
    position: absolute;
    left: 0;
    top: 790px;
    width: 728px;
    margin: 0;
    font-family: "Lato", sans-serif;
    font-weight: 400;
    color: var(--paper);
  }
  .slogan span { position: absolute; white-space: nowrap; }
  .slogan .lead { left: 57px; top: 0; font-size: 43px; }
  .slogan .accent { left: 246px; top: 36px; font-size: 50px; color: var(--leaf); }
  .slogan .close { left: 542px; top: 92px; font-size: 40px; }
  .doc-type {
    position: absolute;
    left: 0;
    width: 728px;
    top: 1098px;
    margin: 0;
    text-align: center;
    font-family: "Lato", sans-serif;
    font-style: italic;
    font-size: 48px;
    color: var(--paper);
  }
  .doc-type .soft { color: var(--mist); }
  .sector-tabs {
    position: absolute;
    top: 0;
    right: 0;
    height: 1200px;
    display: flex;
  }
  .tab {
    height: 100%;
    display: flex;
    justify-content: center;
  }
  .tab span {
    writing-mode: vertical-rl;
    font-family: "Open Sans", sans-serif;
    font-size: 12px;
    padding-top: 6px;
    white-space: nowrap;
  }
  .tab-construction { width: 26px; background: var(--leaf); color: var(--ink); }
  .tab-transport { width: 24px; background: var(--paper); color: var(--ink); }
  .tab-hotel { width: 22px; background: var(--ink); color: var(--paper); }
  .tab-retail { width: 21px; background: var(--paper); color: var(--ink); }
  .tab-housing { width: 27px; background: var(--leaf); color: var(--ink); }
</style>
</head>
<body>
  <main class="cover">
    <div class="brand-mark" aria-hidden="true"></div>
    <h1 class="brand-name">VELTIQ</h1>
    <p class="services-line">REPAIR · RESTORE · RESURFACE</p>
    <p class="slogan">
      <span class="lead">Cutting cost with</span>
      <span class="accent">the environment</span>
      <span class="close">in mind</span>
    </p>
    <p class="doc-type">Company <span class="soft">Brochure</span></p>
    <nav class="sector-tabs" aria-label="Sectors">
      <div class="tab tab-construction"><span>Construction</span></div>
      <div class="tab tab-transport"><span>Public Transport</span></div>
      <div class="tab tab-hotel"><span>Hotel &amp; Leisure</span></div>
      <div class="tab tab-retail"><span>Retail/Businesses</span></div>
      <div class="tab tab-housing"><span>Housing Association</span></div>
    </nav>
  </main>
</body>
</html>
```